Carpet cleaning company focused on high quality needs business cards

We are a growing company that just merged with another company and need to design a new business card. We do both residential as well as commercial cleaning. We do carpet, tile & grout, upholstery, hard floors, and stain & pet odor removal. We treat our customers like family and strive to achieve outstanding results with every job.

```html
<!DOCTYPE html>
<html lang="en">
<head>
<meta charset="utf-8">
<title>Ray's Fresh Floor Cleaning – Business Card</title>
<link href="https://fonts.googleapis.com/css2?family=Open+Sans:wght@600;700;800&display=swap" rel="stylesheet">
<style>
  :root {
    --backdrop: #3b3b3d;
    --card-white: #ffffff;
    --card-grey: #e6e6e6;
    --brand-red: #c4262b;
    --brand-red-dark: #a81f24;
    --ink: #1d1d1d;
    --illus-blue: #2f6f9a;
    --illus-tan: #b08a4a;
  }
  html, body {
    margin: 0;
    width: 1200px;
    height: 900px;
    overflow: hidden;
    background: var(--backdrop);
  }
  .business-card {
    position: absolute;
    left: 100px;
    top: 165px;
    width: 1000px;
    height: 570px;
    border-radius: 40px;
    overflow: hidden;
    background: linear-gradient(135deg, var(--card-white) 0%, var(--card-white) 45%, var(--card-grey) 100%);
    font-family: "Open Sans", sans-serif;
    color: var(--ink);
    box-shadow: 0 6px 20px rgba(0,0,0,0.35);
  }
  .red-band {
    position: absolute;
    inset: 0;
    width: 1000px;
    height: 570px;
  }
  .mascot-illustration {
    position: absolute;
    left: 500px;
    top: 125px;
    width: 300px;
    height: 415px;
    border-radius: 20px;
    background: linear-gradient(170deg, #e9eef2 0%, var(--illus-blue) 45%, var(--illus-tan) 75%, var(--brand-red) 100%);
    opacity: 0.85;
  }
  .brand-name {
    position: absolute;
    right: 60px;
    top: 38px;
    margin: 0;
    font-weight: 800;
    font-size: 28px;
    line-height: 1.05;
    text-transform: uppercase;
    color: var(--ink);
  }
  .contact {
    position: absolute;
    left: 60px;
    top: 105px;
  }
  .contact-name {
    margin: 0;
    font-weight: 800;
    font-size: 32px;
    color: var(--brand-red);
    letter-spacing: 0.5px;
  }
  .contact-title {
    margin: 0;
    font-weight: 700;
    font-size: 20px;
    text-transform: uppercase;
  }
  .contact-phone {
    margin: 20px 0 0;
    font-weight: 700;
    font-size: 21px;
  }
  .divider {
    width: 100px;
    height: 7px;
    margin-top: 30px;
    background: var(--brand-red);
  }
  .services {
    position: absolute;
    left: 62px;
    top: 295px;
    width: 270px;
    margin: 0;
    padding: 0;
    list-style: none;
    font-weight: 700;
    font-size: 22px;
    line-height: 26px;
    text-transform: uppercase;
  }
  .services li {
    padding-left: 18px;
    text-indent: -18px;
  }
  .services li::before {
    content: "• ";
  }
  .website {
    position: absolute;
    right: 16px;
    bottom: 60px;
    writing-mode: vertical-rl;
    transform: rotate(180deg);
    font-weight: 600;
    font-size: 19px;
    color: var(--card-white);
    letter-spacing: 0.5px;
  }
</style>
</head>
<body>
  <div class="business-card">
    <svg class="red-band" viewBox="0 0 1000 570" aria-hidden="true">
      <defs>
        <linearGradient id="bandFill" x1="0" y1="1" x2="1" y2="0">
          <stop offset="0" stop-color="var(--brand-red-dark)"/>
          <stop offset="1" stop-color="var(--brand-red)"/>
        </linearGradient>
      </defs>
      <polygon points="0,555 1000,250 1000,570 0,570" fill="url(#bandFill)"/>
    </svg>

    <div class="mascot-illustration" role="img" aria-label="Cartoon cleaning technician in cap and blue shirt holding up a carpet cleaning wand with hose, red starburst behind"></div>

    <p class="brand-name">Ray's Fresh<br>Floor Cleaning</p>

    <div class="contact">
      <p class="contact-name">MARTIN HOLLOWER</p>
      <p class="contact-title">Managing Director</p>
      <p class="contact-phone">5550 123 456</p>
      <div class="divider"></div>
    </div>

    <ul class="services">
      <li>Carpet</li>
      <li>Tile &amp; Grout</li>
      <li>Upholstery</li>
      <li>Hard Floors</li>
      <li>Stain &amp; Pet Odor Removal</li>
    </ul>

    <span class="website">raysfreshfloor.com</span>
  </div>
</body>
</html>
```